Business cards for the RL Group

We are looking for a template for our new business cards for our company that we can edit ourselves.
You will find our company colors in the logo. the logo on the back and on the front
first name Last Name
position
E-mail address
mobile number
landline number
Companies we have 2 RL Sicherheit GmbH and RL Services GmbH
address
Lindenbergweg 42
22459 Hamburg
www.rlgruppe-nord.de

Something modern, simple but professional

if you have any questions, bring it on.

Sicherheit

Steht in der Beschreibung

F0912C
F2A743
F7CA91
FBE8D2
FDF5EE

• recognition value
• professional
• Playful

```html
<!DOCTYPE html>
<html lang="de">
<head>
<meta charset="utf-8">
<title>RL Gruppe – Visitenkarten</title>
<link rel="stylesheet" href="https://fonts.googleapis.com/css2?family=Anton&family=Montserrat:wght@400;700&display=swap">
<style>
  :root {
    --backdrop: #a3a5ab;
    --card-white: #ffffff;
    --brand-orange: #fd7f0c;
    --brand-grey: #5e5e5e;
    --text-light: #fff6ec;
  }
  html, body {
    margin: 0;
    padding: 0;
    width: 1200px;
    height: 1000px;
    overflow: hidden;
    background: var(--backdrop);
  }
  .canvas {
    position: relative;
    width: 1200px;
    height: 1000px;
  }
  .card {
    position: absolute;
    top: 345px;
    width: 466px;
    height: 301px;
    box-sizing: border-box;
  }
  .card--front {
    left: 98px;
    background: var(--card-white);
  }
  .card--back {
    left: 653px;
    background: var(--brand-orange);
    color: var(--text-light);
  }
  .brand {
    position: absolute;
    display: flex;
    align-items: center;
    gap: 12px;
    font-family: "Anton", sans-serif;
    font-weight: 400;
    text-transform: uppercase;
    line-height: 1;
    white-space: nowrap;
  }
  .brand__dot {
    border-radius: 50%;
    flex: none;
  }
  .card--front .brand {
    left: 120px;
    top: 115px;
    font-size: 58px;
    color: var(--brand-grey);
  }
  .card--front .brand__dot {
    width: 40px;
    height: 40px;
    background: var(--brand-orange);
  }
  .card--back .brand {
    left: 50px;
    top: 130px;
    font-size: 36px;
    gap: 9px;
    color: var(--text-light);
  }
  .card--back .brand__dot {
    width: 26px;
    height: 26px;
    background: var(--text-light);
  }
  .contact {
    position: absolute;
    left: 277px;
    top: 40px;
    font-family: "Montserrat", sans-serif;
  }
  .contact__name {
    margin: 0;
    font-family: "Anton", sans-serif;
    font-weight: 400;
    font-size: 30px;
    line-height: 36px;
  }
  .contact__position {
    margin: 2px 0 0;
    font-size: 11px;
    font-weight: 700;
    letter-spacing: 2px;
  }
  .contact__group {
    margin: 0;
    font-size: 13.5px;
    line-height: 17px;
    letter-spacing: 0.3px;
  }
  .contact__group--phone { margin-top: 34px; }
  .contact__group + .contact__group { margin-top: 16px; }
</style>
</head>
<body>
  <main class="canvas">
    <section class="card card--front" aria-label="Vorderseite">
      <div class="brand">
        <span class="brand__dot"></span>
        <span class="brand__name">RL Gruppe</span>
      </div>
    </section>

    <section class="card card--back" aria-label="Rückseite">
      <div class="brand">
        <span class="brand__dot"></span>
        <span class="brand__name">RL Gruppe</span>
      </div>
      <div class="contact">
        <h1 class="contact__name">Jonas<br>Wetterberg</h1>
        <p class="contact__position">POSITION</p>
        <p class="contact__group contact__group--phone">+49 404 555 0182<br>info@services-rl.de</p>
        <p class="contact__group">Lindenbergweg 42<br>22459 Hamburg</p>
        <p class="contact__group">rlgruppe-nord.de</p>
      </div>
    </section>
  </main>
</body>
</html>
```